VantoMedix website

I have a plumtree hosting website already & have been using wordpress.
See www.vantomedix-example.com
I have a logo's already.
I need a front page "VantoMedix". I have 3 products: (need separate pages)
1) the "GlideDeck" (can't supply images ATM)
2) the "CordKeeper" (several stills below & animation: http://www.videohub-example.com/watch?v=X7KpR2mT9wQ&list=ZPqR8bT_vnxwyLmKcE4D7T_B&feature=share)
3) the "FastWedge" animation here: http://vidhub-example.be/pqwre-Lmm_Z & logo as below

It needs to be corporate & professional looking. VantoMedix is an innovative design house for medical devices.

Reason: Hi Designers, thanks for all your work to date - there have been some great designs. We'll be providing feedback to some of you in the near future. The reason we have extended the deadline is simply that we are too busy with other aspects of the business to focus on this at the moment. Kind regards, the VantoMedix team.

Dear Designers,

VantoMedix apologies for the delay due to our busyness. 
Please help us to understand the process here:
are we getting fully working websites? With multiple pages? Will we be able to modify them?
If not, what is the output?

Kind regards,
the Vanto team.

```html
<!DOCTYPE html>
<html lang="en">
<head>
<meta charset="utf-8">
<title>VantoMedix – Medical Device Design</title>
<link rel="stylesheet" href="https://fonts.googleapis.com/css2?family=Figtree:ital,wght@0,400;0,600;0,700;0,800;1,400&display=swap">
<style>
:root{
  --sky:#dff2fb;
  --blue:#2d9fdb;
  --blue-dark:#1f8dcc;
  --orange:#f36f1c;
  --text:#5d6770;
  --muted:#a7b0b7;
  --heading:#3a4249;
  --nav:#8a96a0;
  --white:#ffffff;
  --green:#4aa82a;
  --red:#e8473a;
  --line:#c9dde8;
}
*{margin:0;padding:0;box-sizing:border-box}
html,body{width:1024px;height:1200px;overflow:hidden}
body{position:relative;background:var(--sky);font-family:"Figtree",sans-serif;color:var(--text)}
.abs{position:absolute}

/* header */
.site-header{left:0;top:0;width:1024px;height:92px;background:var(--sky)}
.brand{left:135px;top:22px;display:flex;align-items:center;gap:8px}
.brand-dot{width:14px;height:14px;border-radius:50%;background:var(--orange)}
.brand-name{font-size:44px;font-weight:800;color:var(--blue);letter-spacing:-1px;line-height:1}
.call{left:644px;top:40px;display:flex;align-items:center;gap:8px;color:var(--orange);font-size:19px}

/* nav */
.main-nav{left:0;top:92px;width:1024px;height:61px;background:var(--white)}
.nav-item{top:0;height:61px;line-height:61px;font-size:10.5px;font-weight:700;color:var(--nav);text-transform:uppercase;letter-spacing:.2px}
.nav-sep{top:10px;width:1px;height:40px;background:#eef1f3}
.nav-active{left:213px;top:13px;width:89px;height:48px;background:var(--blue);color:var(--white);line-height:44px;text-align:center}
.social{top:16px;width:26px;height:26px;border-radius:3px}
.dropdown{left:213px;top:135px;width:121px;height:106px;background:#36aee6;z-index:5}
.drop-item{left:0;width:121px;font-size:10px;color:var(--white);padding-left:17px;font-weight:600}
.drop-active{background:var(--orange)}

/* hero */
.hero{left:0;top:153px;width:1024px;height:430px}
.hero-photo{left:0;top:0;width:1024px;height:430px;background:linear-gradient(110deg,#8ea49a 0%,#c9ced2 35%,#e4e6e8 55%,#6d7f5b 85%,#4f6a3c 100%)}
.hero-curve{left:0;top:0}
.hero-box{left:0;top:109px;width:534px;height:199px;background:rgba(45,159,219,.92)}
.hero-title{left:148px;top:135px;font-size:34px;font-weight:600;color:var(--white)}
.hero-copy{left:148px;top:188px;width:360px;font-size:14px;line-height:20px;color:var(--white);font-weight:600}

/* cards */
.card{top:619px;width:174px;height:279px;background:var(--white);box-shadow:0 1px 2px rgba(0,0,0,.15)}
.card-head{left:0;top:0;width:174px;height:55px;background:linear-gradient(#56b8ea,#2d9fdb);color:var(--white);font-size:13px;font-weight:700;padding:22px 16px 0}
.card-head.centered{text-align:center;padding-left:0;padding-right:0;font-size:15px;letter-spacing:.5px}
.card-media{left:11px;top:72px;width:151px;height:101px;border-radius:2px}
.card-text{left:13px;top:189px;width:152px;font-size:10px;line-height:14.5px;color:var(--muted)}
.read-more{left:13px;top:249px;font-size:9px;font-weight:700;color:var(--blue)}
.contact-line{left:15px;font-size:10px;color:var(--muted)}
.contact-line a{color:var(--blue);text-decoration:none}
.btn-contact{left:26px;top:218px;width:112px;height:36px;border-radius:3px;background:linear-gradient(#fb8a3a,#ef6414);color:var(--white);font-size:12.5px;font-weight:700;text-align:center;line-height:36px;box-shadow:0 1px 2px rgba(0,0,0,.25)}

/* footer */
.footer-rule{left:0;top:918px;width:1024px;height:1px;background:var(--line)}
.foot-h{top:946px;font-size:11px;font-weight:700;color:var(--heading);text-transform:uppercase}
.foot-p{font-size:10px;line-height:17px;color:var(--text)}
.foot-p .tag{color:var(--red)}
.foot-p .ago{color:var(--muted);font-style:italic}
.email-field{left:519px;top:1011px;width:177px;height:29px;border:1px solid #d4dde2;background:var(--white);font-size:10px;color:var(--muted);padding:8px 8px}
.btn-signup{left:519px;top:1052px;width:73px;height:29px;background:var(--green);border-radius:2px;color:var(--white);font-size:10px;font-weight:700;text-align:center;line-height:29px}
.bottom-rule{left:0;top:1151px;width:1024px;height:1px;background:var(--line)}
.copyright{left:135px;top:1170px;font-size:10px;color:var(--nav)}
.legal{left:680px;top:1170px;font-size:10px;font-weight:700;color:var(--heading)}
.legal .hl{color:var(--red)}
.legal .sep{color:var(--muted);font-weight:400;margin:0 4px}
</style>
</head>
<body>

<header class="site-header abs">
  <div class="brand abs"><span class="brand-dot"></span><span class="brand-name">VantoMedix</span></div>
  <div class="call abs">
    <svg width="18" height="18" viewBox="0 0 24 24" fill="none" stroke="#7ab8dd" stroke-width="2"><path d="M6 3l3 5-2 2c1 2 3 4 5 5l2-2 5 3-2 4C10 20 4 14 2 7z"/></svg>
    CALL US +1800.555.0199
  </div>
</header>

<nav class="main-nav abs">
  <div class="nav-item abs" style="left:164px">Home</div>
  <div class="nav-item nav-active abs">Products</div>
  <div class="nav-item abs" style="left:322px">About Us</div>
  <div class="nav-sep abs" style="left:392px"></div>
  <div class="nav-item abs" style="left:411px">Ask Question</div>
  <div class="nav-sep abs" style="left:507px"></div>
  <div class="nav-item abs" style="left:529px">Contact Us</div>
  <div class="social abs" style="left:769px;background:#3b5a9a"></div>
  <div class="social abs" style="left:807px;background:#2aa9e0"></div>
  <div class="social abs" style="left:846px;background:#1a6fa6"></div>
</nav>

<div class="dropdown abs">
  <div class="drop-item abs" style="top:17px;height:24px;line-height:34px">GlideDeck</div>
  <div class="drop-item drop-active abs" style="top:42px;height:32px;line-height:32px">CordKeeper
    <svg class="abs" style="right:9px;top:11px" width="7" height="10" viewBox="0 0 7 10"><path d="M1 1l4 4-4 4" stroke="#fff" stroke-width="2" fill="none"/></svg>
  </div>
  <div class="drop-item abs" style="top:74px;height:32px;line-height:32px">FastWedge</div>
</div>

<section class="hero abs">
  <div class="hero-photo abs" role="img" aria-label="Photo of a smiling paramedic in uniform standing in front of an ambulance"></div>
  <svg class="hero-curve abs" width="1024" height="430" viewBox="0 0 1024 430"><path d="M0 344 Q512 520 1024 344 L1024 430 L0 430 Z" fill="#dff2fb"/></svg>
  <div class="hero-box abs"></div>
  <h1 class="hero-title abs">VantoMedix</h1>
  <p class="hero-copy abs">VantoMedix has created a fully integrated system to help paramedics remove patients from everyday awkward situations: down stairs, around tight corners &amp; out of small rooms.</p>
</section>

<article class="card abs" style="left:138px">
  <div class="card-head abs">GlideDeck</div>
  <div class="card-media abs" role="img" aria-label="Rendering of the GlideDeck device" style="background:linear-gradient(135deg,#b9bde6,#9ea4d6)"></div>
  <p class="card-text abs">Lorem ipsum dolor sit amet, consectetur adipisicing elit, sed do eiusmod tempor incididunt</p>
  <div class="read-more abs">READ MORE</div>
</article>

<article class="card abs" style="left:330px">
  <div class="card-head centered abs">CORDKEEPER</div>
  <div class="card-media abs" role="img" aria-label="Video still of the CordKeeper animation" style="background:linear-gradient(#f4f4f4,#dcdcdc)"></div>
  <p class="card-text abs">Lorem ipsum dolor sit amet, consectetur adipisicing elit, sed do eiusmod tempor incididunt</p>
  <div class="read-more abs">READ MORE</div>
</article>

<article class="card abs" style="left:520px">
  <div class="card-head centered abs" style="font-weight:800">FASTWEDGE</div>
  <div class="card-media abs" role="img" aria-label="Video still of the FastWedge animation" style="background:linear-gradient(90deg,#b8231e,#3a3a3a 40%,#6b2a2a 70%,#b8231e)"></div>
  <p class="card-text abs">Lorem ipsum dolor sit amet, consectetur adipisicing elit, sed do eiusmod tempor incididunt</p>
  <div class="read-more abs">READ MORE</div>
</article>

<aside class="card abs" style="left:712px">
  <div class="card-head abs">Questions? Contact us!</div>
  <div class="contact-line abs" style="top:72px">Phone: (+39) 0100 555 321</div>
  <div class="contact-line abs" style="top:95px">E-mail: <a href="#">info@vantomedix-example.com</a></div>
  <div class="contact-line abs" style="top:130px">Brightfold Studio Ltd.</div>
  <div class="contact-line abs" style="top:153px">4410 Harbor Lane</div>
  <div class="contact-line abs" style="top:176px">Portvale, USA</div>
  <div class="btn-contact abs">Contact Us</div>
</aside>

<div class="footer-rule abs"></div>

<footer>
  <h3 class="foot-h abs" style="left:135px">About</h3>
  <p class="foot-p abs" style="left:135px;top:970px;width:175px">Donec rutrum elit ac arcu bibendum rhoncus in vitae turpis. Quisque fermentum gravida eros non faucibus. Curabitur fermentum, arcu sed cursus commodo.</p>
  <p class="foot-p abs" style="left:135px;top:1065px;line-height:19px">sales@webcraft-example.com<br>+1 (555) 010 - 22 - 33</p>

  <h3 class="foot-h abs" style="left:327px">Recent Tweets</h3>
  <p class="foot-p abs" style="left:327px;top:970px;width:175px;line-height:18px"><span class="tag">@vantomedix</span> Vivamus porta dui dapibus erat egestas semper. In quis sem neque <span class="tag">#paramedic #vanto</span><br><span class="ago">5 minutes ago</span></p>
  <p class="foot-p abs" style="left:327px;top:1050px;width:175px;line-height:18px"><span class="tag">@vantomedix</span> Vivamus porta dui dapibus erat egestas semper. In quis sem neque <span class="tag">#paramedic #vanto</span><br><span class="ago">1 day ago</span></p>

  <h3 class="foot-h abs" style="left:519px">Newsletter Signup</h3>
  <p class="foot-p abs" style="left:519px;top:970px;width:175px">Donec rutrum elit ac arcu bibendum rhoncus in vitae turpis.</p>
  <div class="email-field abs">Enter your e-mail address</div>
  <div class="btn-signup abs">SIGNUP</div>

  <h3 class="foot-h abs" style="left:711px">Navigation</h3>
  <p class="foot-p abs" style="left:711px;top:970px;line-height:21px">Home<br>Products<br>About Us<br>Ask Question<br>Contact Us</p>
  <p class="foot-p abs" style="left:808px;top:970px;line-height:21px">GlideDeck<br>CordKeeper<br>FastWedge</p>

  <div class="bottom-rule abs"></div>
  <div class="copyright abs">Copyright © 2014 VantoMedix. All rights reserved.</div>
  <div class="legal abs">Terms &amp; Conditions<span class="sep">/</span><span class="hl">Privacy Policy</span><span class="sep">/</span>FAQ</div>
</footer>

</body>
</html>
```